Business Card & Stationary Design Project

We are looking for some creative direction for business cards and our stationary.

We are a global logistics firm that has recently changed its name to Marrick Global Logistics and we have a new website due out tomorrow (www.marrick.com.au).

The colours of the company are rich navy tones, I would like to have business cards that fit together to make one picture on the back (possibly an old map of the world??), and the front to be modern contemporary looking.

But I am open to suggestions, so just incorporate our new logo and get going!
Updates

Hi Everyone,

Thank you for all of your designs so far and the time you have put into it.

I have asked many of you for amendments to see if we can get a final product, so with this in mind I am extending the deadline by a few days.

Good luck and thank you once again.

Please message me direct if you need any clarification.

Kind Regards
Colin

Reason: As outlined the extra 3 days is for amendments and changes to the current submissions. Thanks Colin

Industry/Entity Type

Business

```html
<!DOCTYPE html>
<html lang="en">
<head>
<meta charset="utf-8">
<title>Marrick Global Logistics – Business Card</title>
<link rel="stylesheet" href="https://fonts.googleapis.com/css2?family=Arimo:wght@400&display=swap">
<style>
  :root {
    --backdrop: #d9d4cc;
    --frost-light: #f3f1ec;
    --frost-mid: #e4e2dd;
    --frost-blue: #dfe6ee;
    --frost-warm: #ead9d3;
    --card-edge: rgba(255, 255, 255, 0.85);
    --navy: #1f2a5c;
    --band-deep: #1a3663;
    --band-bright: #2c5b92;
    --band-text: #ddd6c6;
    --band-muted: #c9c3b5;
  }
  * { margin: 0; padding: 0; box-sizing: border-box; }
  html, body {
    width: 1200px;
    height: 970px;
    overflow: hidden;
    background: var(--backdrop);
  }
  .canvas {
    position: relative;
    width: 1200px;
    height: 970px;
  }
  .business-card {
    position: absolute;
    left: 100px;
    top: 207px;
    width: 1000px;
    height: 555px;
    border: 1px solid var(--card-edge);
    overflow: hidden;
    background:
      radial-gradient(ellipse 180px 260px at 330px 180px, var(--frost-blue), transparent 70%),
      radial-gradient(ellipse 160px 220px at 860px 170px, var(--frost-blue), transparent 70%),
      radial-gradient(ellipse 260px 90px at 300px 440px, var(--frost-warm), transparent 70%),
      linear-gradient(180deg, var(--frost-light) 0%, var(--frost-mid) 100%);
    box-shadow: 0 18px 40px rgba(60, 50, 40, 0.18);
  }
  .brand {
    position: absolute;
    left: 224px;
    top: 161px;
    display: flex;
    align-items: center;
    gap: 20px;
  }
  .brand-name {
    font-family: 'Arimo', sans-serif;
    font-weight: 400;
    font-size: 28px;
    line-height: 1;
    color: var(--navy);
    white-space: nowrap;
  }
  .brand-dot {
    width: 142px;
    height: 142px;
    border-radius: 50%;
    background: var(--navy);
  }
  .contact-band {
    position: absolute;
    left: 0;
    bottom: 0;
    width: 100%;
    height: 70px;
    background: linear-gradient(90deg, var(--band-deep) 0%, var(--band-bright) 55%, var(--band-deep) 100%);
    font-family: 'Arimo', sans-serif;
  }
  .holder {
    position: absolute;
    left: 19px;
    top: 12px;
    text-align: right;
  }
  .holder-name {
    font-size: 25px;
    color: var(--band-text);
    line-height: 1;
  }
  .holder-role {
    font-size: 15px;
    color: var(--band-muted);
    margin-top: 5px;
  }
  .reach {
    position: absolute;
    right: 35px;
    top: 8px;
    text-align: right;
  }
  .reach-phone {
    font-size: 36px;
    color: var(--band-text);
    line-height: 1;
    letter-spacing: 1px;
  }
  .reach-web {
    font-size: 14px;
    color: var(--band-muted);
    margin-top: 4px;
  }
</style>
</head>
<body>
<main class="canvas">
  <section class="business-card">
    <div class="brand">
      <div class="brand-name">Marrick Global Logistics</div>
      <div class="brand-dot" aria-hidden="true"></div>
    </div>
    <div class="contact-band">
      <div class="holder">
        <div class="holder-name">Devan Rao</div>
        <div class="holder-role">Graphic Designer</div>
      </div>
      <div class="reach">
        <div class="reach-phone">8841307726</div>
        <div class="reach-web">www.corvane.com &nbsp;|&nbsp; x@corvane.com</div>
      </div>
    </div>
  </section>
</main>
</body>
</html>
```